C2C website is looking for a web-designer

Complete description of the project you will find in the file atteched (we updated information there and maybe now it will be easier to understand what it's all about). We are a small team of two people from the Czech Republic and we want to create a united platform in the form of adverts, where people can find smb who will help them to cope with the everyday routine (cooking, cleaning, pet care, house work etc.)
Updates
Project Deadline Extended Reason: We want the designers to have more time for work. Added Wednesday, September 24, 2014
This brief depends on brief 416290 - http://tasks.plumvexa.com/task.aspx?id=416290 (logo design). Both are for the same project. Added Wednesday, September 24, 2014
Industry/Entity Type
House
Number of Pages Required
5+ page
Look and feel
Each slider illustrates characteristics of the customer's brand and the style your logo design should communicate.

```html
<!DOCTYPE html>
<html lang="en">
<head>
<meta charset="utf-8">
<title>Dovedna – Home</title>
<link href="https://fonts.googleapis.com/css2?family=Roboto:wght@400;700&display=swap" rel="stylesheet">
<style>
:root{
  --green:#5aa51f;
  --green-dark:#3f7d12;
  --orange:#f08a12;
  --orange-deep:#d8700a;
  --dark:#2f2f2f;
  --darker:#1c1c1c;
  --black:#0a0a0a;
  --light:#efefef;
  --white:#ffffff;
  --text-muted:#dcdcdc;
}
*{box-sizing:border-box;margin:0;padding:0}
html,body{width:1200px;height:2912px;overflow:hidden}
body{font-family:"Roboto",Arial,sans-serif;background:var(--white);color:var(--white);position:relative}

/* header */
.site-header{position:absolute;left:0;top:0;width:1200px;height:136px;background:var(--white)}
.brand{position:absolute;left:120px;top:30px;display:flex;align-items:center;gap:14px}
.brand-dot{width:40px;height:40px;border-radius:50%;background:var(--green)}
.brand-name{font-size:46px;font-weight:700;color:var(--green)}
.search{position:absolute;left:580px;top:58px;display:flex}
.search-input{width:160px;height:36px;background:var(--darker);color:#ccc;font-size:16px;padding:8px 10px}
.search-btn{width:44px;height:36px;background:#444;display:flex;align-items:center;justify-content:center}
.account{position:absolute;left:900px;top:58px;display:flex;gap:10px}
.account a{height:36px;padding:0 16px;display:flex;align-items:center;font-size:16px;color:var(--white);text-decoration:none;background:var(--darker)}
.account a.register{background:var(--orange)}

/* nav */
.main-nav{position:absolute;left:120px;top:136px;width:960px;height:48px;background:var(--green);display:flex;align-items:stretch}
.main-nav a{color:var(--white);text-decoration:none;font-size:19px;font-weight:700;padding:0 22px;display:flex;align-items:center}
.main-nav a.active{background:var(--white);color:var(--darker)}
.main-nav a.add-advert{margin-left:auto;background:var(--orange);width:130px;justify-content:center;text-align:center;line-height:1.1;font-size:18px;height:64px;margin-top:-8px}

/* hero */
.hero{position:absolute;left:120px;top:184px;width:960px;height:480px}
.hero-visual{position:absolute;inset:0;background:linear-gradient(120deg,#d8dde4 0%,#f4f4f4 40%,#b9c3cf 100%)}
.hero-panel{position:absolute;left:480px;top:44px;width:430px;height:240px;background:rgba(40,40,40,.88);padding:20px 24px}
.hero-panel h2{color:var(--green);font-size:24px;margin-bottom:12px}
.hero-panel p{font-size:14px;line-height:1.45;color:var(--text-muted)}
.btn-orange{display:inline-block;background:var(--orange);color:var(--white);font-size:16px;padding:9px 20px;margin:16px 0 0 120px}
.hero-dots{position:absolute;right:44px;bottom:18px;display:flex;gap:8px}
.hero-dots span{width:10px;height:10px;border-radius:50%;background:#666}
.hero-dots span:first-child{background:var(--white)}

/* categories */
.categories{position:absolute;left:120px;top:664px;width:960px;height:1680px;background:var(--dark)}
.band{position:absolute;left:0;width:960px}
.band.dark{background:linear-gradient(180deg,#3a3a3a,#262626)}
.band.orange{background:linear-gradient(180deg,#e0831a,#c86a0a)}
.ribbon{position:absolute;left:50%;transform:translateX(-50%);height:46px;background:var(--orange);color:var(--white);font-size:24px;font-weight:700;display:flex;align-items:center;justify-content:center;padding:0 60px;clip-path:polygon(0 0,100% 0,96% 50%,100% 100%,0 100%,4% 50%)}
.cat-row{position:absolute;left:0;width:960px;display:grid;grid-template-columns:repeat(4,1fr)}
.cat{display:flex;flex-direction:column;align-items:center;text-align:center}
.cat-badge{width:164px;height:164px;border-radius:50%;background:var(--orange);border:8px dashed #ffb04a;display:flex;align-items:center;justify-content:center}
.cat-icon{width:116px;height:116px;border-radius:50%;background:linear-gradient(160deg,#2a2a2a,#0e0e0e);border:4px solid var(--white)}
.cat h3{font-size:20px;font-weight:400;margin-top:14px}
.cat p{font-size:14px;line-height:1.35;color:var(--text-muted);width:190px;margin-top:8px}
.band.orange .cat p{color:#fff2e0}
.btn-green{margin-top:12px;background:var(--green);color:var(--white);font-size:13px;padding:5px 14px;border:1px solid var(--green-dark)}

/* follow */
.follow{position:absolute;left:120px;top:2344px;width:960px;height:290px;background:var(--light);color:var(--darker);text-align:center}
.follow .ribbon{top:-10px}
.follow-lead{position:absolute;top:60px;width:100%;font-size:18px;color:#444}
.social-list{position:absolute;top:104px;left:180px;width:600px;display:grid;grid-template-columns:repeat(4,1fr)}
.social{display:flex;flex-direction:column;align-items:center}
.social-mark{width:88px;height:88px;border-radius:50%;background:var(--white);border:3px solid #c9c9c9}
.social h4{font-size:18px;font-weight:400;margin-top:10px}
.social span{font-size:13px;color:#555;margin-top:4px}

/* footer */
.site-footer{position:absolute;left:120px;top:2634px;width:960px;height:226px;background:var(--black);display:grid;grid-template-columns:1fr 1fr 1fr;padding:28px 40px;gap:40px}
.site-footer h5{font-size:18px;margin-bottom:10px}
.site-footer p,.site-footer li{font-size:14px;line-height:1.45;color:var(--text-muted);list-style:none}
.news-input{margin-top:10px;height:30px;background:var(--green);color:var(--white);font-size:13px;padding:6px 10px;width:220px}
.news-btn{display:inline-block;margin-top:8px;background:var(--white);color:var(--darker);font-size:13px;font-weight:700;padding:5px 12px}
.cards{display:flex;gap:6px;margin-top:12px}
.cards span{width:34px;height:22px;background:#8a8a8a;border-radius:3px}
.bottom-bar{position:absolute;left:120px;top:2860px;width:960px;height:52px;background:var(--white);color:var(--darker);display:flex;align-items:center;justify-content:space-between;padding:0 40px;font-size:14px}
</style>
</head>
<body>

<header class="site-header">
  <div class="brand"><span class="brand-dot"></span><span class="brand-name">Dovedna</span></div>
  <div class="search">
    <div class="search-input">Search Item</div>
    <div class="search-btn"><svg width="18" height="18" viewBox="0 0 18 18"><circle cx="7.5" cy="7.5" r="5.5" fill="none" stroke="#fff" stroke-width="2"/><line x1="11.5" y1="11.5" x2="16.5" y2="16.5" stroke="#fff" stroke-width="2"/></svg></div>
  </div>
  <div class="account"><a href="#">Login</a><a href="#" class="register">Register</a></div>
</header>

<nav class="main-nav">
  <a href="#" class="active">Home</a>
  <a href="#">Advertisements</a>
  <a href="#">User List</a>
  <a href="#">Gallery</a>
  <a href="#">Articles</a>
  <a href="#">Discussions</a>
  <a href="#" class="add-advert">Add<br>Advert</a>
</nav>

<section class="hero">
  <div class="hero-visual" role="img" aria-label="Photo of a board reading 'Your Ad Here' circled in red marker"></div>
  <div class="hero-panel">
    <h2>Dovedna Services</h2>
    <p>Lorem Ipsum is simply dummy text of the printing and typesetting industry. Lorem Ipsum has been the industry's standard dummy text ever since the 1500s, when an unknown printer took a galley of type and scrambled it to make a type specimen book. It has survived not only five centuries.</p>
    <span class="btn-orange">Register Here</span>
  </div>
  <div class="hero-dots"><span></span><span></span><span></span><span></span></div>
</section>

<section class="categories">
  <div class="band dark" style="top:0;height:430px"></div>
  <div class="band orange" style="top:430px;height:400px"></div>
  <div class="band dark" style="top:830px;height:400px"></div>
  <div class="band orange" style="top:1230px;height:450px"></div>
  <div class="ribbon" style="top:42px">Our Advertisement Categories</div>

  <div class="cat-row" style="top:112px">
    <div class="cat"><div class="cat-badge"><div class="cat-icon" role="img" aria-label="Chef icon"></div></div><h3>Cooking</h3><p>Lorem Ipsum is simply dummy text of the printing</p><span class="btn-green">Click Here</span></div>
    <div class="cat"><div class="cat-badge"><div class="cat-icon" role="img" aria-label="House with tools icon"></div></div><h3>House Work</h3><p>Lorem Ipsum is simply dummy text of the printing</p><span class="btn-green">Click Here</span></div>
    <div class="cat"><div class="cat-badge"><div class="cat-icon" role="img" aria-label="Plant sprouting from soil icon"></div></div><h3>Work in Garden</h3><p>Lorem Ipsum is simply dummy text of the printing</p><span class="btn-green">Click Here</span></div>
    <div class="cat"><div class="cat-badge"><div class="cat-icon" role="img" aria-label="Person walking a dog icon"></div></div><h3>Pet Care</h3><p>Lorem Ipsum is simply dummy text of the printing</p><span class="btn-green">Click Here</span></div>
  </div>

  <div class="cat-row" style="top:484px">
    <div class="cat"><div class="cat-badge"><div class="cat-icon" role="img" aria-label="Baby icon"></div></div><h3>Baby Sitting</h3><p>Lorem Ipsum is simply dummy text of the printing</p><span class="btn-green">Click Here</span></div>
    <div class="cat"><div class="cat-badge"><div class="cat-icon" role="img" aria-label="Teacher at a board icon"></div></div><h3>Tutoring</h3><p>Lorem Ipsum is simply dummy text of the printing</p><span class="btn-green">Click Here</span></div>
    <div class="cat"><div class="cat-badge"><div class="cat-icon" role="img" aria-label="Elderly couple icon"></div></div><h3>Elderly Care</h3><p>Lorem Ipsum is simply dummy text of the printing</p><span class="btn-green">Click Here</span></div>
    <div class="cat"><div class="cat-badge"><div class="cat-icon" role="img" aria-label="Delivery truck icon"></div></div><h3>Transportation</h3><p>Lorem Ipsum is simply dummy text of the printing</p><span class="btn-green">Click Here</span></div>
  </div>

  <div class="cat-row" style="top:882px">
    <div class="cat"><div class="cat-badge"><div class="cat-icon" role="img" aria-label="Handyman with tools icon"></div></div><h3>Handyman</h3><p>Lorem Ipsum is simply dummy text of the printing</p><span class="btn-green">Click Here</span></div>
    <div class="cat"><div class="cat-badge"><div class="cat-icon" role="img" aria-label="Consultant icon"></div></div><h3>Consulting</h3><p>Lorem Ipsum is simply dummy text of the printing</p><span class="btn-green">Click Here</span></div>
    <div class="cat"><div class="cat-badge"><div class="cat-icon" role="img" aria-label="Paint palette icon"></div></div><h3>Art</h3><p>Lorem Ipsum is simply dummy text of the printing</p><span class="btn-green">Click Here</span></div>
    <div class="cat"><div class="cat-badge"><div class="cat-icon" role="img" aria-label="Heart in hands icon"></div></div><h3>Body Care</h3><p>Lorem Ipsum is simply dummy text of the printing</p><span class="btn-green">Click Here</span></div>
  </div>

  <div class="cat-row" style="top:1290px">
    <div class="cat"><div class="cat-badge"><div class="cat-icon" role="img" aria-label="Windmill icon"></div></div><h3>Farming</h3><p>Lorem Ipsum is simply dummy text of the printing</p><span class="btn-green">Click Here</span></div>
    <div class="cat"><div class="cat-badge"><div class="cat-icon" role="img" aria-label="Farm animal icon"></div></div><h3>Animal Products</h3><p>Lorem Ipsum is simply dummy text of the printing</p><span class="btn-green">Click Here</span></div>
    <div class="cat"><div class="cat-badge"><div class="cat-icon" role="img" aria-label="Needle and thread icon"></div></div><h3>Hand made goods</h3><p>Lorem Ipsum is simply dummy text of the printing</p><span class="btn-green">Click Here</span></div>
    <div class="cat"><div class="cat-badge"><div class="cat-icon" role="img" aria-label="24/7 service icon"></div></div><h3>Other Services</h3><p>Lorem Ipsum is simply dummy text of the printing</p><span class="btn-green">Click Here</span></div>
  </div>
</section>

<section class="follow">
  <div class="ribbon">FOLLOW US</div>
  <p class="follow-lead">Get connected with us on social network</p>
  <div class="social-list">
    <div class="social"><div class="social-mark"></div><h4>Friendbook</h4><span>Be Our Friend</span></div>
    <div class="social"><div class="social-mark"></div><h4>Chirper</h4><span>Follow Us</span></div>
    <div class="social"><div class="social-mark"></div><h4>WorkNet</h4><span>Build Professional Network</span></div>
    <div class="social"><div class="social-mark"></div><h4>Circlo</h4><span>Join Our Circle</span></div>
  </div>
</section>

<footer class="site-footer">
  <div>
    <h5>Address</h5>
    <p>Lorem Ipsum is simply dummy text of the printing and type setting industry<br>Phone: +1234567890<br>Email: Lorem Ipsum is simply</p>
  </div>
  <div>
    <h5>Important Links</h5>
    <ul><li>Home</li><li>Advertisement</li><li>Registration</li><li>User Lists</li><li>Gallery</li><li>Articles</li></ul>
  </div>
  <div>
    <h5>News letter</h5>
    <p>Lorem Ipsum is simply dummy text of the printing and typesetting industry.</p>
    <div class="news-input">Your Email</div>
    <span class="news-btn">SUBMIT</span>
    <div class="cards"><span></span><span></span><span></span><span></span></div>
  </div>
</footer>
<div class="bottom-bar">
  <span>Site Map &nbsp;|&nbsp; Privacy &nbsp;|&nbsp; Site Credits</span>
  <span>All Rights Reserved@2014 hello@dovedna-mail.com</span>
</div>

</body>
</html>
```